Website design for a steel buildings

We need a new look for our site www.brindlemoorgroupltd.co.uk, we have listed lots of inspirational images although we are looking for a bespoke site that looks nothing like a theme. We have an in-house development team that will build the website and a UX and design team that will proof all designs.
Colours and layout are down to your imagination and with this brand, we are targeting a commercial market. We require the following pages in both mobile and desktop:
Home
Industrial Buildings
Contact Us

The logo will be supplied by our art team.

Target Market(s)

Commercial

Industry/Entity Type

Construction

Number of Pages Required

3 page

Font styles to use
Sans Serif
Other font styles liked:
• Geomanist

Colors

Designer to choose colors to be used in the design.

Requirements
Must have
• Somthing differant to the original site, new content will be supplied after the design.
• Designs for both desktop and mobile.
• Designs supplied as a PSD, All vector images need the originl AI file
• Images cut up and optimised before file hand over
Nice to have
• Animation
Should not have
• Slider as the hero image

```html
<!DOCTYPE html>
<html lang="en">
<head>
<meta charset="utf-8">
<title>Brindlemoor Group – Steel Building Specialists</title>
<link href="https://fonts.googleapis.com/css2?family=Hind:wght@400;500;600;700&family=Open+Sans:wght@400;600;700&display=swap" rel="stylesheet">
<style>
:root{
  --orange:#e0821f;
  --orange-deep:#c96a12;
  --ink:#222222;
  --text:#4a4a4a;
  --grey-dark:#474747;
  --grey-light:#f6f6f6;
  --white:#ffffff;
  --footer:#1f1f1f;
  --ring:#c9c9c9;
}
*{margin:0;padding:0;box-sizing:border-box}
html,body{width:1200px;height:3442px;overflow:hidden}
body{position:relative;font-family:"Open Sans",Arial,sans-serif;color:var(--text);background:var(--white)}
.abs{position:absolute}
h1,h2,h3,.display{font-family:"Hind",Arial,sans-serif}

/* header */
.site-header{top:0;left:0;width:1200px;height:62px;background:var(--white)}
.brand{left:86px;top:6px;display:flex;align-items:center;gap:10px}
.brand-mark{width:34px;height:34px;background:var(--orange)}
.brand-name{font-family:"Hind",sans-serif;font-weight:700;font-size:34px;color:var(--orange);letter-spacing:.5px;line-height:1}
.call-note{left:585px;top:14px;font-size:12px;font-weight:700;color:var(--ink);line-height:17px;text-align:center}
.call-note span{color:var(--orange)}
.call-number{left:912px;top:14px;display:flex;align-items:center;gap:12px;font-family:"Hind",sans-serif;font-size:26px;color:var(--ink)}

/* hero */
.hero{top:62px;left:0;width:1200px;height:530px;background:
  radial-gradient(ellipse 260px 120px at 560px 260px,rgba(255,214,150,.95) 0%,rgba(240,170,90,.55) 40%,rgba(240,170,90,0) 100%),
  linear-gradient(180deg,rgba(60,70,84,.0) 0%,rgba(60,70,84,0) 55%,rgba(110,114,120,.55) 62%,rgba(200,204,210,.85) 78%,rgba(150,156,164,.9) 100%),
  linear-gradient(180deg,#3f4b5a 0%,#6d7480 30%,#b79a78 48%,#d8b487 54%,#8e8f92 66%,#c9cdd2 100%)}
.hero-band{top:206px;left:0;width:690px;height:127px;background:rgba(20,20,20,.35)}
.hero-title{left:86px;top:228px;font-size:48px;font-weight:700;color:var(--white);line-height:1.1}
.hero-sub{left:94px;top:292px;font-size:17px;color:var(--white)}

/* finance band */
.finance{top:592px;left:0;width:1200px;height:160px;background:var(--orange);text-align:center;color:var(--white)}
.finance h2{margin-top:33px;font-size:36px;font-weight:700;line-height:1.1}
.finance p{font-size:15px;font-weight:700;line-height:25px}
.finance-pointer{top:752px;left:582px;width:0;height:0;border-left:18px solid transparent;border-right:18px solid transparent;border-top:18px solid var(--orange);z-index:2}

/* sectors */
.sectors{top:752px;left:0;width:1200px;height:487px;background:var(--grey-light)}
.section-title{width:1200px;text-align:center;font-size:34px;font-weight:600;color:var(--ink)}
.sector{width:210px;text-align:center}
.sector-photo{width:202px;height:202px;border-radius:50%;margin:0 auto}
.sector-label{margin-top:30px;font-size:17px;color:var(--ink)}
.sector.is-active .sector-photo{border:4px solid var(--orange)}
.sector.is-active .sector-label{color:var(--orange)}

/* about */
.about p{left:126px;width:952px;text-align:center;font-size:15px;line-height:26px;color:var(--text)}

/* services */
.services-panel{top:1716px;left:0;width:429px;height:376px;background:var(--orange);color:var(--white)}
.services-title{left:96px;top:1750px;font-size:38px;font-weight:400;color:var(--white);letter-spacing:1px}
.services-sub{left:96px;top:1800px;width:320px;font-size:13px;line-height:19px;color:var(--white)}
.service-item{left:85px;width:344px;height:42px;display:flex;align-items:center;gap:18px;padding-left:16px;font-family:"Hind",sans-serif;font-size:15px;color:var(--white);letter-spacing:.5px;background:var(--orange-deep)}
.service-item.is-current{background:var(--grey-dark)}
.service-item.is-muted{color:#f5c89a}
.services-copy{top:1716px;left:429px;width:771px;height:376px;background:var(--grey-light)}
.services-copy h2{position:absolute;left:37px;top:46px;font-size:32px;font-weight:600;color:var(--ink)}
.services-copy p{position:absolute;left:37px;width:650px;font-size:15px;line-height:26px;color:var(--text)}

/* quote steps */
.steps-line{top:2389px;left:241px;width:667px;height:2px;background:var(--ring)}
.step-ring{width:162px;height:162px;border-radius:50%;border:2px solid var(--ring);background:var(--white);display:flex;align-items:center;justify-content:center}
.step-core{width:140px;height:140px;border-radius:50%;display:flex;align-items:center;justify-content:center;background:var(--grey-dark)}
.step-core.is-primary{background:var(--orange)}
.step-text{width:250px;text-align:center;font-size:15px;line-height:23px;color:var(--text)}

/* map */
.map{top:2718px;left:0;width:1200px;height:368px;background:
  radial-gradient(ellipse 300px 160px at 260px 120px,rgba(214,226,200,.8),rgba(214,226,200,0)),
  radial-gradient(ellipse 360px 180px at 960px 230px,rgba(222,230,236,.9),rgba(222,230,236,0)),
  linear-gradient(135deg,#eceee3 0%,#e4e7da 50%,#eceee4 100%)}
.map-pin{left:710px;top:2890px}

/* contact bar */
.contact-bar{top:3086px;left:0;width:1200px;height:100px;background:var(--orange);color:var(--white)}
.contact-cta{top:3110px;width:600px;text-align:center;font-family:"Hind",sans-serif;font-weight:700;font-size:18px;line-height:33px;color:var(--white)}
.contact-divider{top:3086px;left:599px;width:2px;height:100px;background:rgba(255,255,255,.35)}

/* footer */
.site-footer{top:3186px;left:0;width:1200px;height:256px;background:var(--footer)}
.social{top:3254px;left:0;width:1200px;display:flex;justify-content:center;gap:18px}
.social span{width:22px;height:22px;background:#3a3a3a;transform:rotate(45deg)}
.footer-nav{top:3316px;left:0;width:1200px;display:flex;justify-content:center;gap:26px;font-size:11px;font-weight:700;color:var(--white);letter-spacing:.3px}
.legal{left:0;width:1200px;text-align:center;font-size:11px;color:#a0a0a0}
</style>
</head>
<body>

<header class="site-header abs">
  <div class="brand abs"><span class="brand-mark"></span><span class="brand-name">BRINDLEMOOR GROUP</span></div>
  <div class="call-note abs">PREFER TO TALK? <span>FREE FROM ALL MOBILE'S</span><br>OUR LINES ARE OPEN UNTIL 6PM TODAY</div>
  <div class="call-number abs">
    <svg width="24" height="24" viewBox="0 0 24 24" fill="none" stroke="#e0821f" stroke-width="1.8"><path d="M5 3h4l2 5-2.5 1.5a11 11 0 0 0 6 6L16 13l5 2v4a2 2 0 0 1-2 2A16 16 0 0 1 3 5a2 2 0 0 1 2-2z"/></svg>
    0345 000 1290
  </div>
</header>

<section class="hero abs" role="img" aria-label="Photograph of a steel frame building under construction with stacked steel decking sheets at sunset"></section>
<div class="hero-band abs"></div>
<h1 class="hero-title abs">Steel Building Specialists</h1>
<p class="hero-sub abs">We are a competitive &amp; reliable steel building specialist</p>

<section class="finance abs">
  <h2>There's no such thing as can't!</h2>
  <p>Spread the cost with a low interest rate. Typically starting at 4.8%</p>
  <p>98% Acceptance rate on all domestic and commercial work from £100 to £500k</p>
</section>

<section class="sectors abs"></section>
<div class="finance-pointer abs"></div>
<h2 class="section-title abs" style="top:838px">Steel Building Specialists?</h2>
<div class="sector abs" style="left:83px;top:927px"><div class="sector-photo" role="img" aria-label="Photograph of a steel roof frame for a domestic building" style="background:radial-gradient(circle at 50% 70%,#9aa3ab 0%,#b8c4cf 35%,#d6e6f2 70%,#c3d8e8 100%)"></div><div class="sector-label">Domestic</div></div>
<div class="sector abs is-active" style="left:347px;top:927px"><div class="sector-photo" role="img" aria-label="Photograph of the inside of an agricultural steel barn" style="background:radial-gradient(circle at 50% 45%,#d7dde3 0%,#8994a0 30%,#4f5a66 60%,#9c9a92 85%,#b3ae9f 100%)"></div><div class="sector-label">Agricultural</div></div>
<div class="sector abs" style="left:620px;top:927px"><div class="sector-photo" role="img" aria-label="Photograph of a commercial steel frame structure" style="background:radial-gradient(circle at 40% 40%,#f1f2f3 0%,#d5d8db 45%,#9aa0a6 80%,#7f858b 100%)"></div><div class="sector-label">Commercial</div></div>
<div class="sector abs" style="left:897px;top:927px"><div class="sector-photo" role="img" aria-label="Illustration of building plans for a planning application" style="background:radial-gradient(circle at 50% 55%,#ffffff 0%,#e9eef3 40%,#c4d1dd 80%,#a9bccd 100%)"></div><div class="sector-label">Planning Application</div></div>

<section class="about">
  <h2 class="section-title abs" style="top:1298px">Let us take care of your project</h2>
  <p class="abs" style="top:1373px">Specialising in Steel Buildings – with over 15 years experience in the industry you are in the right hands. We can provide cold-rolled and hot-rolled steel frames as well as bespoke buildings with custom cladding and roof options. We provide only the best quality products using the best software available within the industry. Every building is custom designed to fit your purpose so you can be sure that your product is unique just for you.</p>
  <p class="abs" style="top:1503px">Our success and our reputation is dependent on the positive feedback and satisfaction of our clients. Whether you require our Steel Building Specialists to install a new building, extend an existing one or carry out a repair, there is no job too small or too large for us. All works come with a full guarantee on all our installations, and are carried out to your specification millermetre perfect.</p>
</section>

<section class="services-panel abs"></section>
<h2 class="services-title abs display">SERVICES</h2>
<p class="services-sub abs">Steel buildings designed to order. Fastest way to plan and start your build.</p>
<div class="service-item is-current abs" style="top:1865px">
  <svg width="20" height="20" viewBox="0 0 20 20" fill="none" stroke="#fff" stroke-width="1.4"><rect x="3" y="3" width="8" height="15"/><rect x="11" y="8" width="6" height="10"/><path d="M5 6h4M5 9h4M5 12h4"/></svg>DOMESTIC BUILDINGS</div>
<div class="service-item is-muted abs" style="top:1925px">
  <svg width="20" height="20" viewBox="0 0 20 20" fill="none" stroke="#f5c89a" stroke-width="1.4"><rect x="3" y="3" width="8" height="15"/><rect x="11" y="8" width="6" height="10"/><path d="M5 6h4M5 9h4M5 12h4"/></svg>AGRICULTURAL BUILDINGS</div>
<div class="service-item is-muted abs" style="top:1986px">
  <svg width="20" height="20" viewBox="0 0 20 20" fill="none" stroke="#f5c89a" stroke-width="1.4"><rect x="3" y="3" width="8" height="15"/><rect x="11" y="8" width="6" height="10"/><path d="M5 6h4M5 9h4M5 12h4"/></svg>COMMERCIAL BUILDINGS</div>

<section class="services-copy abs">
  <h2>Let us take care of your project</h2>
  <p style="top:108px">We are happy dealing directly with architects, engineers, contractors, business owners and end users alike to ensure that your requirements are met. So if you are interested in steel building specialists then we can help. We work across the UK and source only the best to ensure you get the best value for money. After completion we then continue to support you through the lifetime of your guarantee and beyond ensuring it is maintained correctly to extend the life of the building. This is why people come to us at Harlowen, the most trusted name in the construction industry.</p>
  <p style="top:300px">"Let us take care of the things that you shoudnt have to"</p>
</section>

<h2 class="section-title abs" style="top:2190px">Are you looking for a quote?</h2>
<div class="steps-line abs"></div>
<div class="step-ring abs" style="left:162px;top:2309px"><div class="step-core is-primary">
  <svg width="62" height="62" viewBox="0 0 62 62" fill="none" stroke="#fff" stroke-width="3"><path d="M14 6h26l8 8v42H14z"/><path d="M22 20h18M22 28h18M22 36h10"/><path d="M32 46l6 6 12-14"/></svg>
</div></div>
<div class="step-ring abs" style="left:504px;top:2309px"><div class="step-core">
  <svg width="66" height="56" viewBox="0 0 66 56" fill="none" stroke="#fff" stroke-width="3"><ellipse cx="32" cy="28" rx="22" ry="17"/><path d="M26 14h12"/><path d="M18 42v8h7v-5M40 45v5h7v-8"/><circle cx="44" cy="24" r="1.5" fill="#fff"/><path d="M54 26h6v6h-6"/></svg>
</div></div>
<div class="step-ring abs" style="left:827px;top:2309px"><div class="step-core">
  <svg width="60" height="60" viewBox="0 0 60 60" fill="none" stroke="#fff" stroke-width="3"><rect x="10" y="28" width="9" height="24"/><path d="M19 30l9-12v-8a4 4 0 0 1 6 2l-2 12h14a4 4 0 0 1 4 5l-4 17a4 4 0 0 1-4 3H19"/><path d="M40 6l2-4M46 10l4-2M34 4V0"/></svg>
</div></div>
<p class="step-text abs" style="left:118px;top:2494px">Fill in our quick form by clicking here and your enquiry will be sent across to us right away, sit back and relax. We will soon be in-touch within 48 hours</p>
<p class="step-text abs" style="left:460px;top:2494px">In most cases you will recieve a rough quote over the phone if possible. Then lets chat face to face over a cup of coffee.</p>
<p class="step-text abs" style="left:783px;top:2494px">Review your quote, and air out any queries you may have. Once happy lets agree a date that suits both parties - Leave feedback its that simple.</p>

<section class="map abs" role="img" aria-label="Road map showing the office location"></section>
<svg class="map-pin abs" width="34" height="48" viewBox="0 0 34 48"><path d="M17 0C7.6 0 0 7.6 0 17c0 12 17 31 17 31s17-19 17-31C34 7.6 26.4 0 17 0z" fill="#555"/><circle cx="17" cy="17" r="6" fill="#e6e8dc"/></svg>

<section class="contact-bar abs"></section>
<div class="contact-divider abs"></div>
<p class="contact-cta abs" style="left:0">PREFER TO SPEAK, LETS HAVE A CHAT<br>0345 000 1290</p>
<p class="contact-cta abs" style="left:600px">NO NEED TO WAIT, CONTACT US BY FORM<br>CLICK HERE</p>

<footer class="site-footer abs"></footer>
<div class="social abs"><span></span><span></span><span></span><span></span></div>
<nav class="footer-nav abs"><span>HOME</span><span>ABOUT US</span><span>FREE QUOTATION</span><span>CONTACT US</span></nav>
<p class="legal abs" style="top:3346px">© 2017 Brindlemoor Group Ltd. All rights reserved.</p>
<p class="legal abs" style="top:3372px">Terms, conditions, features, availability, pricing, fees, service and support options subject to change without notice.</p>

</body>
</html>
```